Website for premium health insurance and concierge medicine

This is a brand new website for Brask Insurance Services that specializes in Health Insurance and Concierge Medicine for high net-worth and affluent individuals and families. Through this website, clients will be able to learn about products and services, submit applications, and complete self enrollment forms. The website needs to have a premium look & feel that will appeal to a discerning high net-worth individual.

I’m looking for 4 pages in total to begin with. I’m also looking for a designer who will be interested in continuing to build out this new site further over the next few months.

The headline for each page is listed below:

Page 1: HOME PAGE
“Premium Healthcare | Bespoke Concierge Services | Absolute Peace of Mind.”

Page 2: HEALTH INSURANCE
“Premium Healthcare | Elevated.”

Page 3: CONCIERGE MEDICINE
“Personalized Medicine | At-Home Concierge Care | Your Private Physician, 24/7.”

Page 4: DENTAL & VISION
“Your Smile | Your Vision | Perfected.”

Here are several links to existing websites that can be used as design inspiration:

https://vantromhealth.com
https://www.pelvix.org/specialties-services/other-programs-services/concierge-medicine
https://wardelmdnx.com

More generally speaking, I like a clean, modern, dutch style of websites. Here’s an unrelated site that has a good design:

https://www.morvathis.com

Here are a few additional phrases and keywords that will help inspire the design:

Premium Health Insurance
Executive Health Insurance
Concierge Medicine
24/7 access dedicated concierge team
Integrative Concierge Care

I will upload logo files below, here are the font & colors information:

Font: Trajan Pro Bold
Colors:
Blue: hex code: 0071BD, Rgb code: 0, 113, 189  cmyk code: 87,53,0,0
Gray: hex code: #666666, Rgb code: 102,102,102 cmyk code: 60,51,51,20

```html
<!DOCTYPE html>
<html lang="en">
<head>
<meta charset="utf-8">
<title>Dental &amp; Vision | Brask Insurance Services</title>
<link href="https://fonts.googleapis.com/css2?family=Cormorant+Garamond:wght@400;500;600&family=Lato:wght@300;400;700&display=swap" rel="stylesheet">
<style>
:root{
  --blue:#0071bd;
  --gray:#666666;
  --ink:#2a2f36;
  --line:#d9dde2;
  --paper:#ffffff;
  --dark:#1c1d20;
  --footer:#222326;
  --muted:#9a9ea4;
}
*{box-sizing:border-box;margin:0;padding:0}
html,body{width:1200px;height:2504px;overflow:hidden}
body{position:relative;background:var(--paper);font-family:"Lato",sans-serif;color:var(--gray)}
.abs{position:absolute}
.serif{font-family:"Cormorant Garamond",serif}

/* header */
.site-header{left:0;top:0;width:1200px;height:44px}
.brand{left:50px;top:8px;display:flex;align-items:center;gap:8px}
.brand-mark{width:14px;height:14px;border-radius:50%;background:var(--blue)}
.brand-name{font-family:"Lato",sans-serif;font-weight:700;font-size:13px;color:var(--blue);letter-spacing:.5px}
.nav{right:40px;top:12px;display:flex;align-items:center;gap:26px;font-size:11px;color:var(--ink)}
.btn-login{background:var(--blue);color:#fff;border-radius:3px;padding:4px 16px;font-size:10px}
.search{width:110px;height:20px;border:1px solid var(--line);border-radius:10px;font-size:9px;color:var(--muted);padding:4px 10px}

.page-title{left:56px;top:92px;font-size:38px;font-weight:500;color:var(--ink)}

.hero{left:40px;top:152px;width:1120px;height:384px;
  background:linear-gradient(120deg,#1e5f78 0%,#7fc0d4 30%,#e9d8d6 55%,#f1b9c2 70%,#4f8aa0 100%)}

.tagline{left:0;top:552px;width:1200px;text-align:center;font-size:26px;color:var(--ink)}
.intro{left:330px;top:606px;width:540px;text-align:center;font-size:10px;line-height:1.6}

.services{left:96px;top:676px;width:1008px;display:grid;grid-template-columns:1fr 1fr;column-gap:80px;row-gap:40px}
.service-head{display:flex;justify-content:space-between;align-items:center;border-bottom:1px solid var(--line);padding-bottom:8px}
.service-title{font-family:"Cormorant Garamond",serif;font-size:22px;color:var(--ink)}
.arrow-box{width:26px;height:26px;border:1px solid var(--gray);display:flex;align-items:center;justify-content:center}
.service-text{font-size:10px;margin-top:10px;line-height:1.5}

.feature-img-a{left:600px;top:1010px;width:530px;height:256px;background:linear-gradient(90deg,#c9d6df,#e8e4df 55%,#9fb9cc)}
.feature-a{left:160px;top:1064px;width:380px}
.feature-img-b{left:78px;top:1276px;width:450px;height:250px;background:linear-gradient(90deg,#e9e5e1,#d2cbc4 60%,#8a7a72)}
.feature-b{left:620px;top:1424px;width:380px}
.feature-title{font-family:"Cormorant Garamond",serif;font-size:20px;font-weight:600;color:var(--ink);margin-bottom:12px}
.feature-text{font-size:10px;line-height:1.6}

.cta{left:0;top:1590px;width:1200px;height:666px;background:linear-gradient(110deg,#0d0d0f 0%,#3a3b3e 45%,#6f7073 62%,#151517 100%)}
.cta-title{left:0;top:1808px;width:1200px;text-align:center;font-size:30px;color:#fff}
.cta-text{left:420px;top:1860px;width:360px;text-align:center;font-size:10px;line-height:1.6;color:#d8d8d8}
.cta-btn{left:486px;top:1978px;width:228px;height:32px;background:#4a4b4e;color:#fff;font-size:11px;display:flex;align-items:center;justify-content:center}

.site-footer{left:0;top:2256px;width:1200px;height:248px;background:var(--footer)}
.footer-brand{left:70px;top:2300px;display:flex;align-items:center;gap:10px}
.footer-brand .brand-name{color:#fff;font-size:16px}
.footer-cols{left:410px;top:2296px;display:flex;gap:110px}
.footer-col h4{font-size:10px;color:#fff;font-weight:700;margin-bottom:14px}
.footer-col li{list-style:none;font-size:9px;color:var(--muted);margin-bottom:9px}
.copyright{left:0;top:2468px;width:1200px;text-align:center;font-size:9px;color:var(--muted)}
</style>
</head>
<body>

<header class="abs site-header">
  <div class="abs brand"><span class="brand-mark"></span><span class="brand-name">Brask Insurance Services</span></div>
  <nav class="abs nav">
    <span>Health Insurance</span><span>Concierge Medicine</span><span>Dental &amp; Vision</span>
    <span class="btn-login">Login</span><span class="search">Search</span>
  </nav>
</header>

<h1 class="abs page-title serif">Dental &amp; Vision</h1>
<div class="abs hero" role="img" aria-label="Woman in tinted glasses inside a bright modern clinic corridor"></div>

<h2 class="abs tagline serif">Your Smile &nbsp;|&nbsp; Your Vision</h2>
<p class="abs intro">Your smile and eyesight are more than just aesthetics; they are reflections of your confidence, lifestyle, and well-being. At Brask Insurance Services, we provide exclusive dental and vision coverage ensuring access to world-renowned specialists, premier treatments, and cutting-edge technology for those who expect only the best.</p>

<section class="abs services">
  <div class="service">
    <div class="service-head"><span class="service-title">VIP Access to the Leading Specialists</span><span class="arrow-box"><svg width="12" height="12" viewBox="0 0 12 12"><path d="M2 10L10 2M4 2h6v6" stroke="#666" fill="none"/></svg></span></div>
    <p class="service-text">Receive treatment from top-tier cosmetic dentists, periodontologists, and vision experts.</p>
  </div>
  <div class="service">
    <div class="service-head"><span class="service-title">Cosmetics &amp; Restorative Dentistry</span><span class="arrow-box"><svg width="12" height="12" viewBox="0 0 12 12"><path d="M2 10L10 2M4 2h6v6" stroke="#666" fill="none"/></svg></span></div>
    <p class="service-text">Enjoy a flawless smile with whitening, veneers, implants, and state-of-the-art dental procedures.</p>
  </div>
  <div class="service">
    <div class="service-head"><span class="service-title">Laser Vision Correction &amp; Premium Eyewear</span><span class="arrow-box"><svg width="12" height="12" viewBox="0 0 12 12"><path d="M2 10L10 2M4 2h6v6" stroke="#666" fill="none"/></svg></span></div>
    <p class="service-text">Benefit from LASIK, PRK, and designer eyewear selections tailored to your needs.</p>
  </div>
  <div class="service">
    <div class="service-head"><span class="service-title">Preventative &amp; Advanced Treatments</span><span class="arrow-box"><svg width="12" height="12" viewBox="0 0 12 12"><path d="M2 10L10 2M4 2h6v6" stroke="#666" fill="none"/></svg></span></div>
    <p class="service-text">From routine cleanings to specialized oral and vision care, we cover it all.</p>
  </div>
</section>

<div class="abs feature-img-a" role="img" aria-label="Optometrist examining a patient's eyes in a bright clinic"></div>
<div class="abs feature-a">
  <h3 class="feature-title">A Perfect Smile &amp; Crystal Clear Vision</h3>
  <p class="feature-text">Whether you need aesthetic enhancements, corrective procedures, or preventative care, our concierge-level service ensures a smooth, stress-free experience. With hand-selected elite providers, you'll receive only the highest quality treatments designed for longevity and excellence.</p>
</div>

<div class="abs feature-img-b" role="img" aria-label="Patient trying on eyeglasses with an eyewear specialist"></div>
<div class="abs feature-b">
  <h3 class="feature-title">Design for Those Who Expect the Best</h3>
  <p class="feature-text">From celebrity-grade dental care to custom vision solutions, our coverage is tailored for affluent individuals and families who seek perfection in every detail.</p>
</div>

<div class="abs cta" role="img" aria-label="Black and white photo of a man in a suit and glasses seated in a luxury car"></div>
<h2 class="abs cta-title serif">See the Difference, Smile with Confidence</h2>
<p class="abs cta-text">Take the next step in elevating your dental and vision care with coverage you can rely on for the world's finest treatments.</p>
<div class="abs cta-btn">Request a Private Consultation</div>

<footer class="abs site-footer"></footer>
<div class="abs footer-brand"><span class="brand-mark"></span><span class="brand-name">Brask Insurance Services</span></div>
<div class="abs footer-cols">
  <div class="footer-col"><h4>Quicklinks</h4><ul><li>Health Insurance</li><li>Concierge</li><li>Dental &amp; Vision</li><li>Login</li></ul></div>
  <div class="footer-col"><h4>Company</h4><ul><li>About Us</li><li>Contact Us</li><li>Careers</li><li>FAQs</li></ul></div>
  <div class="footer-col"><h4>Legal</h4><ul><li>Privacy Policy</li><li>Terms &amp; Conditions</li><li>Disclaimer</li></ul></div>
  <div class="footer-col"><h4>Contact</h4><ul><li>+1 (555) 014-0271</li><li>+1 (555) 014-0388</li><li>info@braskinsurance.com</li></ul></div>
</div>
<p class="abs copyright">© Copyright 2025 Brask Insurance Services. All Rights Reserved.</p>

</body>
</html>
```